Double-sided business card needed - specific brief

We need a double sided business card designed for our company Radiant Trimline. Having lost a lot of weight myself, the back of the card needs to show my before and after pictures. It needs to cover the entire back side of the card. This might be with my two before pictures over set on top of my main after picture or in separate frames. I'll leave that to your artistic consideration. The front needs to have our logo with contact details centred below.

The cards will be printed by PRINTKO.com and will be rectangular, 84mm x 55mm, but with ROUNDED edges. Please therefore present your designs rectangular but with rounded edges if possible.

The card should be designed in LANDSCAPE orientation.

As well as the logo, the front of the card should have the following details:

Moira Blakewell
Weight Loss Motivator with 189lb personal loss
moira@radiant-trimline.example
+44 (0)7700 900418

The website is important so should perhaps be more bold than the rest:
www.radiant-trimline.example

My brand colours are: Pink #CD2366, Light Pink #FD88AD. Blue #1C9CB1, Light Blue #64C4DE

Target Market(s)

Women 30+

Contact Information for Business Card

As description above

Font styles to use
Sans Serif

Requirements
Must have
• Double sided.
• Back side entirely covered with my before and after pictures.
• You may wish to float my before pictures on top of my after picture or add them in different frames. I look forward to seeing your different suggestions.

```html
<!DOCTYPE html>
<html lang="en">
<head>
<meta charset="utf-8">
<title>Radiant Trimline – Business Card</title>
<link href="https://fonts.googleapis.com/css2?family=Tinos:wght@400;700&display=swap" rel="stylesheet">
<style>
  :root {
    --page-bg: #2b2b2d;
    --brand-pink: #cd2366;
    --brand-blue: #1c9cb1;
    --light-blue: #64c4de;
    --text-white: #f4f1ee;
    --card-radius: 22px;
  }
  * { box-sizing: border-box; margin: 0; padding: 0; }
  html, body {
    width: 1200px; height: 930px; overflow: hidden;
    background: var(--page-bg);
    font-family: "Tinos", "Times New Roman", serif;
  }
  .canvas { position: relative; width: 1200px; height: 930px; }

  .card {
    position: absolute;
    width: 620px; height: 406px;
    border-radius: var(--card-radius);
    overflow: hidden;
    box-shadow: 0 18px 40px rgba(0,0,0,.55);
  }
  .card--back  { left: 110px; top: 44px; }
  .card--front { left: 470px; top: 480px; }

  .photo { position: absolute; inset: 0; }
  .photo--before-after {
    background:
      radial-gradient(ellipse 40% 55% at 48% 48%, rgba(150,100,80,.75), transparent 70%),
      linear-gradient(135deg, #3c3029 0%, #5a4438 45%, #6b2a22 80%, #4a1d18 100%);
  }
  .photo--portrait {
    background:
      radial-gradient(ellipse 25% 40% at 62% 35%, rgba(180,160,120,.5), transparent 70%),
      radial-gradient(ellipse 35% 30% at 75% 70%, rgba(30,40,80,.6), transparent 70%),
      linear-gradient(120deg, #1e1d1b 0%, #3b3630 40%, #2d2a28 65%, #3a1d1a 100%);
  }

  .brand-name {
    position: absolute;
    color: var(--brand-pink);
    font-weight: 400;
    text-transform: uppercase;
    letter-spacing: 1px;
    line-height: 1;
    display: flex; align-items: center; gap: 12px;
  }
  .brand-name__dot {
    width: 26px; height: 26px; border-radius: 50%;
    background: var(--brand-pink);
  }
  .card--back .brand-name { left: 0; right: 0; top: 176px; justify-content: center; font-size: 40px; }
  .card--front .brand-name { right: 38px; top: 70px; font-size: 32px; }

  .website-line {
    position: absolute; left: 0; right: 0; bottom: 72px;
    text-align: center; color: var(--text-white);
    font-size: 16px; letter-spacing: .5px;
  }

  .rule { position: absolute; height: 1.5px; background: var(--text-white); }
  .rule--top { left: 330px; right: 20px; top: 160px; }
  .rule--bottom { left: 30px; width: 250px; top: 300px; }

  .person {
    position: absolute; left: 30px; top: 196px;
    color: var(--text-white);
  }
  .person__name {
    color: var(--brand-blue);
    font-size: 34px; text-transform: uppercase; letter-spacing: .5px;
    margin-bottom: 6px;
  }
  .person__role { font-size: 16px; line-height: 1.3; }

  .contact-list {
    position: absolute; left: 30px; top: 314px;
    list-style: none; color: var(--text-white); font-size: 16px;
  }
  .contact-list li { display: flex; align-items: center; gap: 10px; line-height: 1.55; }
  .contact-list svg { width: 13px; height: 13px; fill: none; stroke: var(--light-blue); stroke-width: 2; }
</style>
</head>
<body>
<main class="canvas">

  <section class="card card--back" aria-label="Card back">
    <div class="photo photo--before-after" role="img" aria-label="Before photo of the client in a bridal veil"></div>
    <h2 class="brand-name"><span class="brand-name__dot"></span>Radiant Trimline</h2>
    <p class="website-line">WWW.RADIANT-TRIMLINE.EXAMPLE</p>
  </section>

  <section class="card card--front" aria-label="Card front">
    <div class="photo photo--portrait" role="img" aria-label="After photo of the client seated in a leather armchair"></div>
    <h2 class="brand-name"><span class="brand-name__dot"></span>Radiant Trimline</h2>
    <div class="rule rule--top"></div>
    <div class="person">
      <h1 class="person__name">Moira Blakewell</h1>
      <p class="person__role">Weight Loss Motivator<br>With 189lb personal loss</p>
    </div>
    <div class="rule rule--bottom"></div>
    <ul class="contact-list">
      <li>
        <svg viewBox="0 0 16 16"><path d="M4 1.5l2.5 3-1.5 2a9 9 0 0 0 4.5 4.5l2-1.5 3 2.5-1.5 2.5C7 14 2 9 1.5 3z"/></svg>
        +44 (0)7700 900418
      </li>
      <li>
        <svg viewBox="0 0 16 16"><rect x="1.5" y="3.5" width="13" height="9"/><path d="M1.5 3.5l6.5 5 6.5-5"/></svg>
        moira@radiant-trimline.example
      </li>
      <li>
        <svg viewBox="0 0 16 16"><circle cx="8" cy="8" r="6.5"/><path d="M1.5 8h13M8 1.5c3 3 3 10 0 13M8 1.5c-3 3-3 10 0 13"/></svg>
        www.radiant-trimline.example
      </li>
    </ul>
  </section>

</main>
</body>
</html>
```